Car dent,ding,crease removal. This will be for the Automotive industry, bodywork repair.

I need a double sided business card designing.

Company name is Panel Mender and we remove small car park dents creases and dings.

The card should have sleek car design/outline on it.

The wording Paintless Dent Removal to be on the card.

The background colours used should include Royal blue, black, and a hint of red.

Need a sleek modern look, clean lines.

I really don't want designers going to my website and just copying the car design, I want something new!

Reason: I've put a guaranteed payment on the design now.

Industry/Entity Type

Automotive

Requirements
Must have
• Paintless Dent Removal
Panel Mender
Gareth Holloway
enquiries@panelmender.example.co.uk
07700954316
Covering, Chester, North Wales and the Wirral
Free quotes available
www.panelmender.example.co.uk

```html
<!DOCTYPE html>
<html lang="en">
<head>
<meta charset="utf-8">
<title>Panel Mender – Business Card</title>
<link rel="stylesheet" href="https://fonts.googleapis.com/css2?family=Jost:ital,wght@0,400;0,500;0,600;1,400&family=Arimo:wght@400;700&display=swap">
<style>
  :root {
    --stage: #2b2c2e;
    --card-black: #0b0b0c;
    --card-grey: #3b3b3d;
    --band-grey: #4a4a4c;
    --paper: #ffffff;
    --brand-red: #e1241c;
    --chrome: #cfd3d8;
    --ink: #111111;
    --text-light: #f4f4f4;
    --car-red-light: #e0242a;
    --car-red-dark: #7a0b0f;
  }
  * { box-sizing: border-box; margin: 0; padding: 0; }
  html, body { width: 1200px; height: 900px; overflow: hidden; }
  body {
    background: var(--stage);
    display: flex;
    flex-direction: column;
    align-items: center;
    justify-content: center;
    gap: 40px;
    font-family: "Jost", sans-serif;
  }
  .card {
    position: relative;
    width: 694px;
    height: 400px;
    overflow: hidden;
    box-shadow: 0 8px 24px rgba(0,0,0,.45);
  }

  /* ---------- front ---------- */
  .card--front { background: var(--card-black); }
  .front__panel {
    position: absolute; left: 0; top: 82px; width: 100%; height: 206px;
    background: var(--card-grey);
  }
  .ragged { position: absolute; left: 0; width: 100%; display: block; }
  .front__logo {
    position: absolute; right: 30px; top: 18px;
    font-family: "Jost", sans-serif; font-weight: 600;
    font-size: 50px; letter-spacing: 1px; line-height: 1;
    color: var(--brand-red);
  }
  .tagline {
    position: absolute;
    font-family: "Jost", sans-serif; font-weight: 500; font-style: italic;
    color: var(--chrome); letter-spacing: 2px; line-height: 1;
  }
  .front__tagline { right: 30px; top: 100px; font-size: 32px; }
  .holder__name {
    position: absolute; left: 38px; top: 172px;
    font-size: 31px; font-weight: 400; color: var(--text-light); line-height: 1;
  }
  .holder__role {
    position: absolute; left: 38px; top: 212px;
    font-size: 16px; font-style: italic; color: var(--text-light);
  }
  .car-illustration {
    position: absolute; left: 420px; top: 172px; width: 274px; height: 228px;
    border-top-left-radius: 160px 90px;
    background: radial-gradient(ellipse at 40% 35%, var(--car-red-light), var(--car-red-dark) 80%);
  }
  .contacts {
    position: absolute; left: 38px; top: 294px; list-style: none;
    font-size: 18px; color: var(--text-light);
  }
  .contacts li { display: flex; align-items: center; gap: 10px; height: 30px; }
  .contacts svg { width: 17px; height: 17px; flex: none; }

  /* ---------- back ---------- */
  .card--back { background: var(--paper); }
  .back__band {
    position: absolute; left: 0; top: 108px; width: 100%; height: 168px;
    background: var(--band-grey);
  }
  .back__logo {
    position: absolute; left: 44px; top: 88px;
    font-family: "Jost", sans-serif; font-weight: 600;
    font-size: 46px; letter-spacing: 1px; line-height: 1;
    color: var(--brand-red);
  }
  .back__tagline { left: 44px; top: 180px; font-size: 36px; }
  .back__info {
    position: absolute; left: 38px; top: 280px;
    font-family: "Arimo", sans-serif; color: var(--ink);
  }
  .back__quote { font-size: 22px; font-weight: 700; margin-bottom: 10px; }
  .back__areas-label { font-size: 19px; font-weight: 700; margin-bottom: 4px; }
  .back__areas { font-size: 19px; }
</style>
</head>
<body>

  <section class="card card--front" aria-label="Card front">
    <div class="front__panel"></div>
    <svg class="ragged" style="top:72px;height:16px" viewBox="0 0 694 16" preserveAspectRatio="none" aria-hidden="true">
      <polygon fill="#0b0b0c" points="0,0 694,0 694,10 670,6 650,12 620,5 600,13 575,7 550,12 520,4 495,11 470,6 440,13 410,5 385,12 360,6 330,14 300,6 275,11 250,4 220,12 195,6 170,13 140,5 115,11 90,6 60,13 35,5 15,11 0,7"/>
    </svg>
    <svg class="ragged" style="top:280px;height:16px" viewBox="0 0 694 16" preserveAspectRatio="none" aria-hidden="true">
      <polygon fill="#0b0b0c" points="0,16 694,16 694,8 665,12 640,4 615,10 585,3 560,11 530,5 505,12 475,4 450,10 420,3 395,11 365,5 340,12 310,4 285,10 255,3 230,11 200,5 175,12 145,4 120,10 90,3 65,11 35,5 12,10 0,6"/>
    </svg>

    <h1 class="front__logo">PANEL MENDER</h1>
    <p class="tagline front__tagline">Paintless Dent Removal</p>

    <p class="holder__name">Gareth Holloway</p>
    <p class="holder__role">Proprietor</p>

    <div class="car-illustration" role="img" aria-label="Illustration of a red sports car front"></div>

    <ul class="contacts">
      <li>
        <svg viewBox="0 0 20 20" fill="none" stroke="#f4f4f4" stroke-width="1.4" aria-hidden="true">
          <circle cx="10" cy="10" r="8"/><ellipse cx="10" cy="10" rx="3.5" ry="8"/><line x1="2" y1="10" x2="18" y2="10"/>
        </svg>
        www.panelmender.example.co.uk
      </li>
      <li>
        <svg viewBox="0 0 20 20" fill="none" stroke="#f4f4f4" stroke-width="1.4" aria-hidden="true">
          <circle cx="10" cy="10" r="8"/><circle cx="10" cy="10" r="3"/><path d="M13 10v1.5a2 2 0 0 0 4 0V10"/>
        </svg>
        enquiries@panelmender.example.co.uk
      </li>
      <li>
        <svg viewBox="0 0 20 20" fill="none" stroke="#f4f4f4" stroke-width="1.4" aria-hidden="true">
          <circle cx="10" cy="10" r="8"/><path d="M7 6l1.5 0 .8 2-1 1a5 5 0 0 0 2.7 2.7l1-1 2 .8V13a1 1 0 0 1-1 1A7 7 0 0 1 6 7a1 1 0 0 1 1-1z"/>
        </svg>
        07700954316
      </li>
    </ul>
  </section>

  <section class="card card--back" aria-label="Card back">
    <div class="back__band"></div>
    <svg class="ragged" style="top:96px;height:14px" viewBox="0 0 694 14" preserveAspectRatio="none" aria-hidden="true">
      <polygon fill="#4a4a4c" points="0,14 694,14 694,6 668,9 645,3 620,8 590,2 565,9 535,4 510,10 480,3 455,8 425,2 400,9 370,4 345,10 315,3 290,8 260,2 235,9 205,4 180,10 150,3 125,8 95,2 70,9 40,4 15,8 0,5"/>
    </svg>

    <h2 class="back__logo">PANEL MENDER</h2>
    <p class="tagline back__tagline">Paintless Dent Removal</p>

    <div class="back__info">
      <p class="back__quote">Free quotes available</p>
      <p class="back__areas-label">Covering Areas :</p>
      <p class="back__areas">Chester, North Wales and the Wirral</p>
    </div>
  </section>

</body>
</html>
```